Private Equity Fund needs a powerpoint template

We need a power point presentation template for our recent founded firm, Corvane Partners, a private equity/investment fund (funded by investors, is a firm that buys, holds and sells companies years after) focused in turnaround cases. The presentation should address corporate and financial subjects in a clean/plain way, but as most straightforward way as possible. This is a commercial pitch/flip presentation, is not a presentation with animations to be presented to a mass of people.

We would like that the designer resume the file that we began building (adapted from other funds/advisors of the market) and establish the following according to our logo:
1) a new set of fonts (size levels and type),
2) colors (tables, headers, lines),
3) space available for content (text boxes, tables, pictures or charts) (note left column space in blank)
4) set, our Excel applications to use as default, the color guide that you have you defined
5) white background

Basically, we need to change the items listed above to the "Example.ppt" file uploaded along with those instructions.

The presentation should:
A) rule how the people in our organization should address our messages (guide with size of tables, font and size, colors)
B) pattern a set of slides that could minimize the time for arranging formats, worrying only about the content
C) allow the person who is building the presentation to have options while addressing the message

Dont get too restricted to what we are giving you (the "Example.ppt" file). You may suggest:
i) logo positioning
ii) with or without any vague space (left column space in blank)
iii) space optmization
iv) shades and colors
v) fonts (careful with the wide ones as it does not optimizes space)

I'm uploading:

Target Market(s)

Banks
Investors
Company owners/founders
Funds

Industry/Entity Type

Financial Service

Font styles to use
Other font styles liked:
• Arial Narrow, Arial, trojan

Colors

Designer to choose colors to be used in the design.

Requirements
Must have
• We would like that the designer resume the file that we began building (adapted from other funds/advisors of the market) and establish the following according to our logo:
• 1) a new set of fonts (size levels and type),
• 2) colors (tables, headers, lines),
• 3) space available for content (text boxes, tables, pictures or charts) (note left column space in blank)
• 4) set, our Excel applications to use as default, the color guide that you have you defined
• 5) white background
Nice to have
• Narrow font type
• Space optimization
• Discrete
Should not have
• Animations
• Font size too big
• colored background

```html
<!DOCTYPE html>
<html lang="en">
<head>
<meta charset="utf-8">
<title>Corvane Partners – Slide Template</title>
<link href="https://fonts.googleapis.com/css2?family=Cinzel:wght@500&family=Lato:wght@400;700&display=swap" rel="stylesheet">
<style>
  :root {
    --ink: #111111;
    --body: #222222;
    --rule: #555555;
    --marker: #3a3a3a;
    --brand: #4a4a4a;
    --footer-bg: #333333;
    --footer-text: #ffffff;
    --paper: #ffffff;
  }
  * { margin: 0; padding: 0; box-sizing: border-box; }
  html, body { width: 1200px; height: 900px; overflow: hidden; background: var(--paper); }
  .slide { position: relative; width: 1200px; height: 900px; background: var(--paper); font-family: "Lato", Arial, sans-serif; color: var(--body); }

  .slide-title {
    position: absolute; left: 30px; top: 24px;
    font-family: "Cinzel", "Times New Roman", serif; font-weight: 500;
    font-size: 46px; letter-spacing: 0.5px; color: var(--ink); line-height: 1.2;
  }
  .title-rule { position: absolute; left: 0; top: 86px; width: 570px; height: 2px; background: var(--rule); }

  .brand { position: absolute; right: 24px; top: 30px; display: flex; align-items: center; gap: 12px; }
  .brand-square { width: 40px; height: 40px; background: var(--brand); }
  .brand-name { font-family: "Cinzel", "Times New Roman", serif; font-weight: 500; font-size: 30px; color: var(--brand); line-height: 1; }

  .topic { position: absolute; left: 37px; width: 1140px; }
  .topic-marker { position: absolute; left: 0; top: 2px; width: 40px; height: 42px; background: var(--marker); border-radius: 3px; }
  .topic-heading { margin-left: 64px; font-weight: 700; font-size: 27px; color: var(--ink); line-height: 1.3; }
  .topic-text { margin-left: 64px; margin-top: 4px; font-size: 19.5px; line-height: 37.5px; color: var(--body); }

  .topic-1 { top: 154px; }
  .topic-2 { top: 304px; }
  .topic-3 { top: 470px; }
  .topic-4 { top: 620px; }

  .footer {
    position: absolute; left: 0; bottom: 0; width: 1200px; height: 62px;
    background: var(--footer-bg); color: var(--footer-text);
    display: flex; align-items: center; justify-content: space-between;
    padding: 0 18px 0 15px; font-size: 21px;
  }
</style>
</head>
<body>
<main class="slide">
  <h1 class="slide-title">PROJECT TITLE HERE</h1>
  <div class="title-rule"></div>

  <div class="brand">
    <span class="brand-square"></span>
    <span class="brand-name">Corvane Partners</span>
  </div>

  <section class="topic topic-1">
    <span class="topic-marker"></span>
    <h2 class="topic-heading">Subtext Title Here</h2>
    <p class="topic-text">Lorem ipsum data sit Lorem ipsum data sit Lorem ipsum data sit Lorem ipsum data sit Lorem ipsum data sit Lorem ipsum data sit Lorem ipsum data sit Lorem ipsum data sit Lorem ipsum data sit Lorem ipsum data</p>
  </section>

  <section class="topic topic-2">
    <span class="topic-marker"></span>
    <h2 class="topic-heading">Subtext Title Here</h2>
    <p class="topic-text">Lorem ipsum data sit Lorem ipsum data sit Lorem ipsum data sit Lorem ipsum data sit Lorem ipsum data sit Lorem ipsum data sit Lorem ipsum data sit Lorem ipsum data sit Lorem ipsum data sit Lorem ipsum data sit</p>
  </section>

  <section class="topic topic-3">
    <span class="topic-marker"></span>
    <h2 class="topic-heading">Subtext Title Here</h2>
    <p class="topic-text">Lorem ipsum data sit Lorem ipsum data sit Lorem ipsum data sit Lorem ipsum data sit Lorem ipsum data sit Lorem ipsum data sit Lorem ipsum data sit Lorem ipsum data sit Lorem ipsum data sit Lorem ipsum data</p>
  </section>

  <section class="topic topic-4">
    <span class="topic-marker"></span>
    <h2 class="topic-heading">Subtext Title Here</h2>
    <p class="topic-text">Lorem ipsum data sit Lorem ipsum data sit Lorem ipsum data sit Lorem ipsum data sit Lorem ipsum data sit Lorem ipsum data sit Lorem ipsum data sit Lorem ipsum data sit Lorem ipsum data sit Lorem ipsum data sit</p>
  </section>

  <footer class="footer">
    <span class="footer-copyright">Copyrigh text here</span>
    <span class="footer-page">Page : 02</span>
  </footer>
</main>
</body>
</html>
```